Pebble CCTV A5 Flyer for attracting sales

Looking for an A5 flyer to be designed to advertise 3 specific CCTV packages from my website www.pebblecctv.example. the packages are I - 3 camera solution J - 4 cameras and L - 5 cameras. The background of the flyer should be white as I will be printing these myself on standard white A5 paper. Need to advertise also the business contact details and for it to say somewhere "protect your home with our CCTV packages". Also need to get the message across that we supply and install as well as there being a 1 year onsite warranty with all our packages. If you feel A5 is not big enough then feel free to design on A4
Security Service

```html
<!DOCTYPE html>
<html lang="en">
<head>
<meta charset="utf-8">
<title>Pebble CCTV – A5 Flyer</title>
<link rel="stylesheet" href="https://fonts.googleapis.com/css2?family=Archivo+Black&family=Arimo:wght@400;700&family=Tinos&display=swap">
<style>
  :root {
    --backdrop: #c9c9c9;
    --paper: #ffffff;
    --red: #d3202f;
    --red-dark: #b51825;
    --ink: #1d1d1d;
    --grey: #9a9a9a;
    --light-grey: #dcdcdc;
    --price-red: #d3202f;
    --sky-top: #6f9bd0;
    --sky-low: #c9d7e6;
    --house: #8a8278;
    --garden: #4f5f3a;
  }
  * { box-sizing: border-box; margin: 0; padding: 0; }
  html, body { width: 927px; height: 1200px; overflow: hidden; }
  body { background: var(--backdrop); font-family: "Arimo", Arial, sans-serif; color: var(--ink); position: relative; }

  .flyer { position: absolute; left: 97px; top: 78px; width: 723px; height: 1025px; background: var(--paper); overflow: hidden; }

  .hero-photo {
    position: absolute; left: 0; top: 0; width: 723px; height: 520px;
    background:
      linear-gradient(180deg, transparent 55%, var(--garden) 100%),
      linear-gradient(180deg, var(--sky-top) 0%, var(--sky-low) 42%, var(--house) 70%, var(--garden) 100%);
  }
  .hero-curve { position: absolute; left: 0; top: 0; width: 723px; height: 540px; }

  .headline {
    position: absolute; left: 42px; top: 30px;
    font-family: "Archivo Black", Arial, sans-serif; font-size: 36px; line-height: 47px;
    color: #fff; letter-spacing: 1px;
    text-shadow: 2px 2px 0 #333, -1px -1px 0 #333, 1px -1px 0 #333, -1px 1px 0 #333;
  }

  .brand-box {
    position: absolute; left: 460px; top: 2px; width: 226px; height: 168px; background: var(--paper);
    display: flex; flex-direction: column; align-items: center; justify-content: center; gap: 14px;
  }
  .brand-mark { width: 64px; height: 64px; border-radius: 50%; background: var(--ink); }
  .brand-name { font-weight: 700; font-size: 21px; color: var(--ink); letter-spacing: .3px; }

  .warranty-badge {
    position: absolute; left: 3px; top: 275px; width: 228px; height: 228px; border-radius: 50%;
    background: var(--paper); border: 2px solid var(--red);
    display: flex; flex-direction: column; align-items: center; justify-content: center;
    text-align: center; font-size: 17px; line-height: 23px; color: #222;
  }
  .warranty-badge .big-one { font-family: "Archivo Black", Arial, sans-serif; font-size: 50px; line-height: 48px; color: var(--red); }

  .packages { position: absolute; left: 16px; top: 526px; display: flex; gap: 12px; }
  .package {
    width: 220px; height: 364px; border: 1px dashed #aaa; background: var(--paper);
    box-shadow: 2px 3px 5px rgba(0,0,0,.25); position: relative;
  }
  .package-title {
    height: 46px; background: var(--ink); color: #fff; text-align: center;
    font-weight: 700; font-size: 16.5px; line-height: 22px; padding-top: 2px;
  }
  .features { list-style: none; padding: 7px 6px 0 8px; }
  .features li { display: flex; gap: 6px; font-size: 12.6px; line-height: 13.5px; margin-bottom: 7px; color: #222; }
  .features svg { flex: none; width: 10px; height: 10px; margin-top: 2px; }
  .kit-photo {
    position: absolute; left: 10px; right: 10px; top: 230px; height: 82px;
    background: linear-gradient(180deg, #eeeeee 0%, #d8d8d8 45%, #2a2a2a 70%, #555 100%);
    border-radius: 3px;
  }
  .price-bar {
    position: absolute; left: 0; right: 0; bottom: 0; height: 50px; background: var(--light-grey);
    display: flex; align-items: center; padding-left: 4px; gap: 10px;
  }
  .price-label { font-size: 14.5px; line-height: 16px; color: #333; }
  .price { font-family: "Tinos", "Times New Roman", serif; font-size: 30px; color: var(--price-red); }

  .contact-bar {
    position: absolute; left: 0; top: 924px; width: 723px; height: 84px; background: var(--red);
    color: #fff; display: flex; align-items: center;
  }
  .contact-title { font-size: 34px; width: 285px; padding-left: 18px; }
  .contact-address { font-size: 16px; line-height: 19px; width: 217px; }
  .contact-lines { border-left: 2px solid #fff; height: 62px; padding-left: 14px; font-weight: 700; font-size: 16px; line-height: 29px; display: flex; flex-direction: column; justify-content: center; }
  .footer-strip { position: absolute; left: 0; top: 1008px; width: 723px; height: 17px; background: #2a2a2a; }
</style>
</head>
<body>
<main class="flyer">
  <div class="hero-photo" role="img" aria-label="Photograph of a modern single-storey house with lit entrance and front garden at dusk"></div>
  <svg class="hero-curve" viewBox="0 0 723 540" aria-hidden="true">
    <path d="M0,330 Q330,560 723,318 L723,540 L0,540 Z" fill="#9a9a9a"/>
    <path d="M0,338 Q330,555 723,330 L723,540 L0,540 Z" fill="#d3202f"/>
    <path d="M0,352 Q330,565 723,345 L723,540 L0,540 Z" fill="#ffffff"/>
    <path d="M0,390 Q330,540 723,380" fill="none" stroke="#9a9a9a" stroke-width="14" opacity=".8"/>
    <path d="M0,410 Q330,560 723,400 L723,540 L0,540 Z" fill="#ffffff"/>
  </svg>

  <h1 class="headline">PROTECT YOUR<br>HOME WITH OUR<br>CCTV PACKAGES</h1>

  <div class="brand-box">
    <span class="brand-mark"></span>
    <span class="brand-name">PEBBLE CCTV LTD</span>
  </div>

  <div class="warranty-badge">
    <span>we supply and<br>install as well as<br>there being a</span>
    <span class="big-one">1</span>
    <span>year onsite<br>warranty with all<br>our packages.</span>
  </div>

  <section class="packages">
    <article class="package">
      <h2 class="package-title">[Package I 1080P]<br>3 Camera</h2>
      <ul class="features">
        <li><svg viewBox="0 0 10 10"><path d="M1,5 L4,8 L9,1" fill="none" stroke="#d3202f" stroke-width="2"/></svg><span>DVR Recording Resolution 1920x1080 Full HD 1080p</span></li>
        <li><svg viewBox="0 0 10 10"><path d="M1,5 L4,8 L9,1" fill="none" stroke="#d3202f" stroke-width="2"/></svg><span>4 Channel 1080p DVR</span></li>
        <li><svg viewBox="0 0 10 10"><path d="M1,5 L4,8 L9,1" fill="none" stroke="#d3202f" stroke-width="2"/></svg><span>High quality 1080p Cameras with 40m IR Distance</span></li>
        <li><svg viewBox="0 0 10 10"><path d="M1,5 L4,8 L9,1" fill="none" stroke="#d3202f" stroke-width="2"/></svg><span>2TB hard drive</span></li>
        <li><svg viewBox="0 0 10 10"><path d="M1,5 L4,8 L9,1" fill="none" stroke="#d3202f" stroke-width="2"/></svg><span>HDMI / VGA Ports</span></li>
        <li><svg viewBox="0 0 10 10"><path d="M1,5 L4,8 L9,1" fill="none" stroke="#d3202f" stroke-width="2"/></svg><span>Remote video footage access via a mobile app</span></li>
      </ul>
      <div class="kit-photo" role="img" aria-label="Three white dome cameras above a black DVR recorder"></div>
      <div class="price-bar"><span class="price-label">BUY NOW<br>ONLY FOR</span><span class="price">£ 609.95</span></div>
    </article>

    <article class="package">
      <h2 class="package-title">[Package J 1080P]<br>4 Camera</h2>
      <ul class="features">
        <li><svg viewBox="0 0 10 10"><path d="M1,5 L4,8 L9,1" fill="none" stroke="#d3202f" stroke-width="2"/></svg><span>DVR Recording Resolution 1920x1080 Full HD 1080p</span></li>
        <li><svg viewBox="0 0 10 10"><path d="M1,5 L4,8 L9,1" fill="none" stroke="#d3202f" stroke-width="2"/></svg><span>4 Channel 1080p DVR</span></li>
        <li><svg viewBox="0 0 10 10"><path d="M1,5 L4,8 L9,1" fill="none" stroke="#d3202f" stroke-width="2"/></svg><span>High quality 1080p Cameras with 40m IR Distance</span></li>
        <li><svg viewBox="0 0 10 10"><path d="M1,5 L4,8 L9,1" fill="none" stroke="#d3202f" stroke-width="2"/></svg><span>2TB hard drive</span></li>
        <li><svg viewBox="0 0 10 10"><path d="M1,5 L4,8 L9,1" fill="none" stroke="#d3202f" stroke-width="2"/></svg><span>HDMI / VGA Ports</span></li>
        <li><svg viewBox="0 0 10 10"><path d="M1,5 L4,8 L9,1" fill="none" stroke="#d3202f" stroke-width="2"/></svg><span>Remote video footage access via a mobile app</span></li>
      </ul>
      <div class="kit-photo" role="img" aria-label="Four white dome cameras above a black DVR recorder"></div>
      <div class="price-bar"><span class="price-label">BUY NOW<br>ONLY FOR</span><span class="price">£ 659.95</span></div>
    </article>

    <article class="package">
      <h2 class="package-title">[Package L 1080P]<br>5 Camera</h2>
      <ul class="features">
        <li><svg viewBox="0 0 10 10"><path d="M1,5 L4,8 L9,1" fill="none" stroke="#d3202f" stroke-width="2"/></svg><span>DVR Recording Resolution 1920x1080 Full HD 1080p</span></li>
        <li><svg viewBox="0 0 10 10"><path d="M1,5 L4,8 L9,1" fill="none" stroke="#d3202f" stroke-width="2"/></svg><span>8 Channel 1080p DVR</span></li>
        <li><svg viewBox="0 0 10 10"><path d="M1,5 L4,8 L9,1" fill="none" stroke="#d3202f" stroke-width="2"/></svg><span>High quality 1080p Cameras with 40m IR Distance</span></li>
        <li><svg viewBox="0 0 10 10"><path d="M1,5 L4,8 L9,1" fill="none" stroke="#d3202f" stroke-width="2"/></svg><span>3TB hard drive</span></li>
        <li><svg viewBox="0 0 10 10"><path d="M1,5 L4,8 L9,1" fill="none" stroke="#d3202f" stroke-width="2"/></svg><span>HDMI / VGA Ports</span></li>
        <li><svg viewBox="0 0 10 10"><path d="M1,5 L4,8 L9,1" fill="none" stroke="#d3202f" stroke-width="2"/></svg><span>Remote video footage access via a mobile app</span></li>
      </ul>
      <div class="kit-photo" role="img" aria-label="Five white dome cameras above a black DVR recorder"></div>
      <div class="price-bar"><span class="price-label">BUY NOW<br>ONLY FOR</span><span class="price">£ 759.95</span></div>
    </article>
  </section>

  <footer class="contact-bar">
    <h2 class="contact-title" style="font-weight:400">CONTACT US</h2>
    <address class="contact-address" style="font-style:normal">Pebble CCTV Ltd<br>14 Harbour Lane<br>London E2 5QT<br>Company Reg: 12345678</address>
    <div class="contact-lines">
      <span>E: info@pebblecctv.example</span>
      <span>T: +44 (0)20 7946 0321</span>
    </div>
  </footer>
  <div class="footer-strip"></div>
</main>
</body>
</html>
```